Kampfsport Außenwerbung
Zielgruppe
Kampfsportschule für Kinder, Jugendliche und Erwachsene. Sportarten: Kick-Boxen, Jiu-Jitsu und Tricking
Aufgabenstellung
Ich bräuchte für meine Schaufenster eine schöne Außenwerbung. Beworben werden sollen alle meine Sportarten. Ich lade meinen Flyer hoch, damit im ähnlichen Stil gearbeitet werden kann. Außerdem auch noch andere Beispiele an denen man sich orientieren kann, sowie mein Logo und meine Fensterfront.

```html
<!DOCTYPE html>
<html lang="de">
<head>
<meta charset="utf-8">
<title>Martial Arts Murb – Schaufensterbanner</title>
<link rel="stylesheet" href="https://fonts.googleapis.com/css2?family=Exo+2:ital,wght@0,700;0,800;1,800;1,900&display=swap">
<style>
  :root {
    --page: #f2f2f2;
    --ink: #0d0d0d;
    --ink-soft: #1a1a1a;
    --ghost: #060606;
    --white: #ffffff;
    --red: #d3222b;
    --red-deep: #9b161c;
    --red-dark: #7a1014;
    --blue: #1ba0e2;
    --blue-deep: #0b73c0;
    --blue-dark: #085a99;
  }
  * { box-sizing: border-box; margin: 0; padding: 0; }
  html, body {
    width: 1200px; height: 912px; overflow: hidden;
    background: var(--page);
    font-family: "Exo 2", sans-serif;
  }
  .banner-set {
    position: absolute; left: 305px; top: 100px;
    display: flex; gap: 49px;
  }
  .banner {
    position: relative; width: 270px; height: 713px; overflow: hidden;
    background: radial-gradient(circle at 50% 40%, var(--ink-soft), var(--ink) 70%);
    box-shadow: 4px 6px 12px rgba(0,0,0,.28);
  }
  .banner--red { --accent: var(--red); --accent-deep: var(--red-deep); --accent-dark: var(--red-dark); }
  .banner--blue { --accent: var(--blue); --accent-deep: var(--blue-deep); --accent-dark: var(--blue-dark); }

  .banner__shapes { position: absolute; inset: 0; }

  .brand {
    position: absolute; top: 58px; left: 0; right: 0;
    display: flex; align-items: center; justify-content: center; gap: 6px;
    font-weight: 800; font-size: 15px; color: var(--white);
  }
  .brand__dot { width: 10px; height: 10px; border-radius: 50%; background: var(--accent); }

  .ghost-name {
    position: absolute; top: 120px; left: 40px; right: 20px;
    font-weight: 900; font-style: italic; font-size: 48px; line-height: 1.05;
    color: var(--ghost); text-align: center;
  }

  .photo {
    position: absolute; left: 22px; right: 22px; top: 150px; height: 340px;
    clip-path: polygon(0 0, 100% 0, 100% 81%, 0 99%);
    background: linear-gradient(160deg, #d9c2a8 0%, #efece8 45%, #e6d24a 85%);
  }
  .banner--blue .photo {
    left: 0; right: 0; top: 160px;
    clip-path: polygon(0 0, 100% 0, 100% 78%, 0 97%);
    background: linear-gradient(150deg, #e04a8c 0%, #2a2a2a 40%, #d8244a 60%, #e8d23a 85%);
  }

  .headline {
    position: absolute; right: 26px; left: 20px;
    font-weight: 900; font-style: italic; color: var(--white);
    text-shadow: 2px 2px 0 var(--ink), -1px -1px 0 var(--ink), 1px -1px 0 var(--ink), -1px 1px 0 var(--ink);
    transform: rotate(-3deg);
  }
  .headline__main { display: block; line-height: .9; }
  .headline__sub { display: block; font-size: 21px; line-height: 1.1; margin-top: 6px; }

  .banner--red .headline { top: 470px; text-align: right; }
  .banner--red .headline__main { font-size: 70px; }
  .banner--red .headline__sub { text-align: left; padding-left: 6px; }

  .banner--blue .headline { top: 487px; text-align: center; left: 14px; right: 14px; }
  .banner--blue .headline__main { font-size: 56px; }
  .banner--blue .headline__sub { font-size: 27px; margin-top: 0; }

  .banner__rule {
    position: absolute; left: 0; right: 0; top: 650px; height: 3px; background: var(--white);
  }
  .contact {
    position: absolute; left: 0; right: 0; top: 656px; bottom: 0;
    background: var(--accent-deep);
    display: flex; align-items: center; justify-content: center; gap: 8px;
    color: var(--white); font-weight: 800;
  }
  .banner--red .contact { font-size: 21px; }
  .banner--blue .contact { font-size: 16px; background: var(--blue-deep); }
  .contact__icon { width: 22px; height: 22px; }
</style>
</head>
<body>
<main class="banner-set">

  <article class="banner banner--red">
    <svg class="banner__shapes" viewBox="0 0 270 713" aria-hidden="true">
      <polygon points="0,0 50,0 110,62 0,122 0,84 58,62 8,0" fill="var(--accent-deep)"/>
      <polygon points="18,0 60,0 110,62 90,62" fill="var(--accent)"/>
      <polygon points="270,0 220,0 160,62 270,122 270,84 212,62 262,0" fill="var(--accent-deep)"/>
      <polygon points="252,0 210,0 160,62 180,62" fill="var(--accent)"/>
      <polygon points="0,400 30,470 0,480" fill="var(--accent-dark)"/>
      <polygon points="0,483 270,421 270,656 0,656" fill="var(--accent-deep)"/>
      <polygon points="0,483 270,421 270,470 0,540" fill="var(--accent)"/>
    </svg>
    <div class="brand"><span class="brand__dot"></span>Martial Arts MURB</div>
    <div class="ghost-name">Martial<br>Arts<br>Murb</div>
    <div class="photo" role="img" aria-label="Foto: Mädchen im weißen Karateanzug mit gelbem Gürtel in Kampfhaltung"></div>
    <h2 class="headline">
      <span class="headline__main">Jiu<br>Jitsu</span>
      <span class="headline__sub">Selbstvertadigung</span>
    </h2>
    <div class="banner__rule"></div>
    <p class="contact">
      <svg class="contact__icon" viewBox="0 0 24 24" aria-hidden="true"><path d="M6.6 10.8a15 15 0 0 0 6.6 6.6l2.2-2.2a1 1 0 0 1 1-.25 11.4 11.4 0 0 0 3.6.57 1 1 0 0 1 1 1V20a1 1 0 0 1-1 1A17 17 0 0 1 3 4a1 1 0 0 1 1-1h3.5a1 1 0 0 1 1 1c0 1.25.2 2.45.57 3.57a1 1 0 0 1-.25 1z" fill="var(--white)"/></svg>
      0152 / 3098 1146
    </p>
  </article>

  <article class="banner banner--blue">
    <svg class="banner__shapes" viewBox="0 0 270 713" aria-hidden="true">
      <polygon points="0,0 50,0 110,62 0,122 0,84 58,62 8,0" fill="var(--accent-deep)"/>
      <polygon points="18,0 60,0 110,62 90,62" fill="var(--accent)"/>
      <polygon points="270,0 220,0 160,62 270,122 270,84 212,62 262,0" fill="var(--accent-deep)"/>
      <polygon points="252,0 210,0 160,62 180,62" fill="var(--accent)"/>
      <polygon points="0,470 270,421 270,656 0,656" fill="var(--accent-deep)"/>
      <polygon points="0,470 270,421 270,480 0,540" fill="var(--accent)"/>
    </svg>
    <div class="brand"><span class="brand__dot" style="background: var(--red)"></span>Martial Arts MURB</div>
    <div class="ghost-name">Martial<br>Arts<br>Murb</div>
    <div class="photo" role="img" aria-label="Foto: Mädchen mit rotem Kopfschutz und pinken Handschuhen beim Kick"></div>
    <h2 class="headline">
      <span class="headline__main">Kick<br>Boxen</span>
      <span class="headline__sub">Sportkarate</span>
    </h2>
    <div class="banner__rule"></div>
    <p class="contact">info@martial-arts-murb.de</p>
  </article>

</main>
</body>
</html>
```